Business Cards

Now that we have a fantastic logo, we need business cards designed for our organization.
We'd like a design that uses our logo and is very creative and eye catching. It should have the following copy, in addition to our logo. It can be standard business card size, or smaller.
Gather. Nurture. Make Art.
1128 Pelham Avenue
Willits, California
Mendocino County
California
United States of America
url: www.larkspurrowguild.org
twitter: #larkspurcraft
facebook, linkedin, google+, and tumblr: larkspur row guild
email: info@larkspurrowguild

```html
<!DOCTYPE html>
<html lang="en">
<head>
<meta charset="utf-8">
<title>Larkspur Row Guild — Business Cards</title>
<link rel="stylesheet" href="https://fonts.googleapis.com/css2?family=Raleway:wght@300;400&display=swap">
<style>
  :root {
    --backdrop: #2b2b2b;
    --card: #ededeb;
    --ink: #6a6a6a;
    --accent: #ee9c57;
    --accent-faint: rgba(238, 156, 87, 0.28);
    --social: #4aa3df;
  }
  * { box-sizing: border-box; margin: 0; padding: 0; }
  html, body {
    width: 1200px; height: 960px; overflow: hidden;
    background: var(--backdrop);
    font-family: "Raleway", sans-serif;
    font-weight: 300;
    color: var(--ink);
  }
  .sheet {
    position: relative; width: 1200px; height: 960px;
    display: flex; flex-direction: column; align-items: center; justify-content: center; gap: 60px;
  }
  .card {
    position: relative; width: 580px; height: 330px;
    background: var(--card);
    box-shadow: 0 10px 30px rgba(0,0,0,0.45);
    overflow: hidden;
  }
  /* Front */
  .card--front { display: flex; flex-direction: column; align-items: center; justify-content: center; }
  .brand-mark { width: 96px; height: 118px; background: var(--accent); }
  .brand-name {
    margin-top: 10px; font-size: 22px; font-weight: 400; letter-spacing: 0.5px; color: var(--ink);
  }
  .tagline {
    margin-top: 12px; font-size: 19px; letter-spacing: 0.5px; color: var(--accent);
  }
  /* Back */
  .backdrop-mark {
    position: absolute; left: 218px; top: 0; width: 130px; height: 330px;
    background: var(--accent-faint);
  }
  .address {
    position: absolute; left: 28px; top: 60px;
    font-size: 15px; line-height: 1.55; font-style: normal;
  }
  .contact {
    position: absolute; right: 28px; top: 40px; text-align: right;
    font-size: 15px; line-height: 1.5;
  }
  .contact-row { display: flex; align-items: center; justify-content: flex-end; gap: 8px; margin-bottom: 10px; }
  .dot { width: 14px; height: 14px; border-radius: 50%; background: var(--social); }
  .square { width: 14px; height: 14px; background: var(--social); }
  .mail-label { color: var(--accent); }
  .web {
    position: absolute; left: 0; right: 0; bottom: 30px; text-align: center;
    font-size: 16px;
  }
</style>
</head>
<body>
  <main class="sheet">
    <section class="card card--front" aria-label="Card front">
      <div class="brand-mark" role="img" aria-label="Organization emblem"></div>
      <p class="brand-name">larkspur row guild</p>
      <p class="tagline">Gather. Nurture. Make Art.</p>
    </section>

    <section class="card card--back" aria-label="Card back">
      <div class="backdrop-mark" role="img" aria-label="Faint organization emblem"></div>
      <address class="address">
        1128 Pelham Avenue<br>
        Willits, California<br>
        Mendocino County<br>
        California<br>
        United States of America
      </address>
      <div class="contact">
        <div class="contact-row"><span class="dot"></span><span>#larkspurcraft</span></div>
        <div class="contact-row"><span class="square"></span><span>larkspur row guild</span></div>
        <div class="contact-row"><span><span class="mail-label">mail:</span>info@larkspurrowguild</span></div>
      </div>
      <p class="web">www.larkspurrowguild.org</p>
    </section>
  </main>
</body>
</html>
```